Car rental website design for a UAE car rental company

This project is about creating a new website design for a car rental company located in Dubai (United Arab Emirates), I opened the same project a few months ago but I didn't receive a lot of appealing entries so I closed it but this time I am marking the project as guaranteed to avoid such situation again, if you have already provided a design before then please re-submit again on this project so that it is considered while reviewing all the designs

A few important things:

1- We need a simple non-complex design
2- The final deliverable would be 2 screens (PSD, JPEG ... etc), the first screen is for the home page and the second screen is for an internal page
3- The home page must have a section that end users can use to rent a car online directly from the home page instead of going into some inner pages
4- The current website is very old and not very appealing so avoid creating a similar design (www.quarvin-drive.example)
5- The name is Quarvin but the company rents normal cars (no Limousin cars will be rented) so avoid adding any fancy cars in the images/graphics used in the design, just normal end users cars
6- The expected pages would be: home, About us, Our team, Strategy, Contact us and links to social media pages
7- The attachments include the company's logo and some screens from other car rental companies that provide online rentals/payments

If you have any questions please feel free to ask and please note that we will need the designs urgently

Thanks

Target Market(s)

Dubai - United Arab Emirates

Industry/Entity Type

It Company

Number of Pages Required

2 page

Font styles to use
Sans Serif

Requirements
Must have
• Check the project details
Nice to have
Should not have

```html
<!DOCTYPE html>
<html lang="en">
<head>
<meta charset="utf-8">
<title>Quarvin Rent A Car</title>
<link rel="stylesheet" href="https://fonts.googleapis.com/css2?family=Arimo:ital,wght@0,400;0,700;1,700&family=Gelasio&display=swap">
<style>
:root{
  --brand:#a6003a;
  --brand-dark:#8c0031;
  --brand-deep:#8f0032;
  --grey-band:#dde0de;
  --strip:#d3d5d4;
  --ink:#222;
  --white:#fff;
  --btn-grey:#7a7a7a;
  --btn-dark:#333;
}
*{box-sizing:border-box;margin:0;padding:0}
html,body{width:891px;height:1200px;overflow:hidden;background:var(--white)}
body{position:relative;font-family:"Arimo",Arial,sans-serif;color:var(--ink)}
.abs{position:absolute}

.top-band{left:0;top:0;width:891px;height:89px;background:var(--brand)}
.nav-band{left:0;top:89px;width:891px;height:51px;background:var(--brand-dark)}
.grey-strip{left:0;top:140px;width:891px;height:10px;background:var(--strip)}

.brand-box{left:124px;top:0;width:171px;height:140px;background:var(--white);text-align:center}
.brand-mark{display:block;width:44px;height:44px;margin:28px auto 6px;background:var(--brand)}
.brand-name{font-size:25px;color:var(--btn-grey);font-weight:400;line-height:26px}
.brand-sub{font-size:12px;color:var(--brand);letter-spacing:2px;line-height:14px}

.header-illustration{left:356px;top:16px;width:94px;height:50px;border-radius:6px;background:var(--brand-deep)}
.tagline{left:467px;top:14px;color:var(--white);font-family:"Gelasio",Georgia,serif}
.tagline .l1{font-size:26px;line-height:32px}
.tagline .l2{font-size:17px;line-height:22px;margin-left:39px}

.main-nav{left:370px;top:89px;height:51px;display:flex;align-items:center;list-style:none}
.main-nav li{color:var(--white);font-size:16.5px;padding:0 19px;line-height:51px;border-right:1px solid rgba(0,0,0,.18)}
.main-nav li:last-child{border-right:none}
.main-nav .home{padding:0 19px 0 10px}

.hero{left:0;top:150px;width:891px;height:374px;background:linear-gradient(180deg,#2f8fd0 0%,#7cc4e8 45%,#cfe7ef 75%,#6a7f8f 100%)}
.booking{left:479px;top:199px;width:339px;height:260px;background:var(--brand);border-radius:7px;color:var(--white)}
.booking h2{position:absolute;left:31px;top:12px;font-family:"Gelasio",Georgia,serif;font-weight:400;font-size:42px}
.booking .rule{position:absolute;left:19px;width:300px;height:2px;background:var(--white)}
.field-label{position:absolute;left:34px;font-size:12.5px}
.field{position:absolute;left:165px;width:137px;height:21px;background:var(--white);color:var(--ink);font-size:12.5px;line-height:21px;padding-left:9px;border:1px solid #ccc}
.field svg{position:absolute;right:5px;top:4px}
.book-btn{position:absolute;left:165px;top:211px;width:83px;height:21px;background:var(--white);color:var(--ink);font-size:12.5px;line-height:21px;text-align:center;border:1px solid #ccc}

.welcome{left:0;top:524px;width:891px;height:208px;background:var(--grey-band)}
.welcome h1{position:absolute;left:157px;top:21px;font-size:25px;color:var(--brand);font-weight:700}
.welcome .car-photo{position:absolute;left:87px;top:68px;width:223px;height:110px;border-radius:12px;background:linear-gradient(180deg,#d4d7d8,#9a9ea1 60%,#c9cccd)}
.welcome p{position:absolute;left:327px;top:57px;width:452px;font-size:14px;line-height:17px}
.welcome .lead{position:absolute;left:327px;top:143px;font-size:15.5px;font-style:italic;font-weight:700;color:var(--brand)}
.read-more{position:absolute;width:87px;height:17px;background:var(--brand);color:var(--white);font-size:10px;font-weight:700;line-height:17px;text-align:center}

.section-title{position:absolute;color:var(--brand);font-weight:700}
.body-text{position:absolute;font-size:11.5px;font-weight:700;line-height:18.5px}
.pill{position:absolute;width:119px;height:27px;color:var(--white);font-size:15px;line-height:27px;text-align:center}
.pill.grey{background:var(--btn-grey)}
.pill.dark{background:var(--btn-dark)}
.city-photo{left:513px;top:760px;width:272px;height:107px;border:1px solid #aaa;background:linear-gradient(180deg,#9fb6d3 0%,#c9cfd5 55%,#5e6b78 100%)}

.footer-band{left:0;top:1031px;width:891px;height:96px;background:var(--brand)}
.footer-nav{position:absolute;left:101px;top:37px;display:flex;list-style:none;font-size:14px;color:#f2c9d6}
.footer-nav li{padding:0 9px;border-right:1px solid var(--white);line-height:20px}
.footer-nav li:first-child{padding-left:0;color:var(--white);font-weight:700}
.footer-nav li:last-child{border-right:none}
.call{position:absolute;left:511px;top:30px;font-size:27px;color:var(--white)}

.copyright{left:101px;top:1137px;font-size:14px;color:var(--ink)}
.social{left:516px;top:1132px;display:flex;gap:11px}
.social span{display:block;width:24px;height:24px;border-radius:3px}
</style>
</head>
<body>

<div class="abs top-band"></div>
<div class="abs nav-band"></div>
<div class="abs grey-strip"></div>

<div class="abs brand-box">
  <span class="brand-mark"></span>
  <div class="brand-name">Quarvin</div>
  <div class="brand-sub">Rent A Car</div>
</div>

<div class="abs header-illustration" role="img" aria-label="Small car illustration"></div>

<div class="abs tagline">
  <div class="l1">Experience an extra mile</div>
  <div class="l2">of comfort, pleasure &amp; leisure from the best</div>
</div>

<ul class="abs main-nav">
  <li class="home"><svg width="14" height="13" viewBox="0 0 14 13"><path d="M1 7 L7 1 L13 7 M3 6 V12 H11 V6" fill="none" stroke="#c9a0ad" stroke-width="1.6"/></svg></li>
  <li>About</li>
  <li>Our Team</li>
  <li>Strategy</li>
  <li>Contact</li>
</ul>

<div class="abs hero" role="img" aria-label="Smiling woman leaning on a car in front of the Dubai skyline"></div>

<form class="abs booking">
  <h2>Book Your Car</h2>
  <div class="rule" style="top:66px"></div>
  <div class="field-label" style="top:85px">Pick-up Location from</div>
  <div class="field" style="top:83px">Dubai Air Port
    <svg width="11" height="9" viewBox="0 0 11 9"><path d="M0 0 H11 L5.5 9 Z" fill="#888"/></svg>
  </div>
  <div class="field-label" style="top:123px">Pick-up Date</div>
  <div class="field" style="top:121px">27th Mar. 2015
    <svg width="15" height="13" viewBox="0 0 15 13"><rect x="0.5" y="0.5" width="14" height="12" fill="none" stroke="#aaa"/><path d="M5 0 V13 M10 0 V13 M0 4.5 H15 M0 8.5 H15" stroke="#aaa"/></svg>
  </div>
  <div class="field-label" style="top:163px">Pick-up Time</div>
  <div class="field" style="top:161px">07 : 30 AM
    <svg width="14" height="14" viewBox="0 0 14 14"><circle cx="7" cy="7" r="7" fill="#999"/><path d="M4 7 L6.5 9 L10 4.5" fill="none" stroke="#fff" stroke-width="1.5"/></svg>
  </div>
  <div class="rule" style="top:195px"></div>
  <div class="book-btn">Book</div>
</form>

<section class="abs welcome">
  <h1>Welcome to Quarvin Book your car now</h1>
  <div class="car-photo" role="img" aria-label="Silver car"></div>
  <p>As Dubai is expected to welcome millions of tourists and visitors, car rental industry is believed to escalate more rapidly in the region. Over the past five years, demands for car rentals in Dubai has been augmenting at a healthy pace and is currently registering a growth rate of 20 to 25 percent per year.</p>
  <div class="lead">The swift economic growth and.....</div>
  <div class="read-more" style="left:327px;top:170px">Read More</div>
</section>

<h3 class="section-title" style="left:128px;top:760px;font-size:20px">Servicess</h3>
<p class="body-text" style="left:131px;top:797px;width:262px">Quarvin offers a comprehensive range of services including daily, short term and long term rental, chauffeur drive services for every purpose and budget.</p>
<div class="read-more" style="left:308px;top:874px">Read More</div>

<h3 class="section-title" style="left:128px;top:911px;font-size:20px">Rates, Terms &amp; Conditions</h3>
<div class="pill grey" style="left:129px;top:945px">Rates</div>
<div class="pill dark" style="left:276px;top:945px">Insurance</div>
<div class="pill grey" style="left:129px;top:983px">Documents</div>
<div class="pill grey" style="left:276px;top:983px">General</div>

<div class="abs city-photo" role="img" aria-label="Dubai city skyline at dusk"></div>
<h3 class="section-title" style="left:514px;top:875px;font-size:18px">Mission &amp; Vision</h3>
<p class="body-text" style="left:514px;top:906px;width:294px;font-size:11.5px;line-height:18px">To be one of the leading auto leasing company in the fast growing economy and tourism industry of the emirate of Dubai and play alongside....</p>
<div class="read-more" style="left:514px;top:973px">Read More</div>

<footer class="abs footer-band">
  <ul class="footer-nav">
    <li>Home</li>
    <li>About</li>
    <li>Our Team</li>
    <li>Strategy</li>
    <li>Contact</li>
  </ul>
  <div class="call">Call Us: +971 40 555 0182</div>
</footer>

<div class="abs copyright">© Copyright 2011, Quarvin. All rights reserved.</div>
<div class="abs social">
  <span style="background:#3fa9e0"></span>
  <span style="background:#3b5a9a"></span>
  <span style="background:#555"></span>
  <span style="background:#f3a21b"></span>
</div>

</body>
</html>
```